Commercial Bakery needs packing design for a Bread Bag.

Dorne's Bakery needs a design for a bread bag to be distributed to grocery stores. We make all kinds of breads and want this packaging to represent our company. We would like the packaging to be black and white with a fun/bubbly modern design. I have attached a few ideas of what I am looking for.
There are 5 different products. Packaging must be the same for each product except for corresponding product name, bar code and nutrional facts.
Product names:
Coconut Cream Bread
Cream Bread
Potato Rolls
Roll ups
Coconut & Raisin Bread

Our products are packaged in a 11” x 8” poly bag.
I will open 5 contracts with whoever’s design I select. I will then provide nutritional facts, barcodes for items once a contract is selected. Thank you!!

Target Market(s)

Grocery stores

Industry/Entity Type

Bakery

Requirements
Must have
• Black and White (off whites are ok)
Should not have
• Color

```html
<!DOCTYPE html>
<html lang="en">
<head>
<meta charset="utf-8">
<title>Dorne's Bakery – Coconut Cream Bread Bag</title>
<link href="https://fonts.googleapis.com/css2?family=Bebas+Neue&family=Lobster&display=swap" rel="stylesheet">
<style>
  :root {
    --stage: #ababab;
    --window: #a1a1a1;
    --window-light: #b4b4b4;
    --paper: #ededec;
    --ink: #1e1e1e;
    --wheat-fill: #2a2a2a;
  }
  html, body {
    margin: 0;
    padding: 0;
    width: 1200px;
    height: 960px;
    overflow: hidden;
    background: var(--stage);
  }
  .bag {
    position: absolute;
    left: 302px;
    top: 71px;
    width: 596px;
    height: 818px;
    background: var(--paper);
  }
  .top-band {
    position: absolute;
    left: 0; top: 0;
    width: 100%; height: 55px;
    background: var(--paper);
  }
  .double-rule {
    position: absolute;
    height: 2px;
    border-top: 1.5px solid var(--ink);
    border-bottom: 1.5px solid var(--ink);
  }
  .top-band .double-rule { left: 0; right: 0; top: 36px; }
  .window {
    position: absolute;
    left: 0; top: 55px;
    width: 100%; height: 406px;
    background: radial-gradient(ellipse at 60% 40%, var(--window-light), var(--window) 70%);
  }
  .panel {
    position: absolute;
    left: 0; top: 461px;
    width: 100%; height: 357px;
    background: var(--paper);
  }
  .panel .rule-left { left: 0; width: 200px; top: 35px; }
  .panel .rule-right { right: 0; width: 200px; top: 35px; }
  .panel .rule-bottom { left: 0; right: 0; top: 320px; }
  .brand-name {
    position: absolute;
    left: 0; right: 0;
    top: 8px;
    text-align: center;
    font-family: "Lobster", cursive;
    font-size: 36px;
    color: var(--ink);
    margin: 0;
    line-height: 1.6;
  }
  .product {
    position: absolute;
    left: 0; right: 0;
    top: 112px;
    text-align: center;
    color: var(--ink);
  }
  .product-flavour {
    display: flex;
    justify-content: center;
    align-items: center;
    gap: 12px;
    font-family: "Lobster", cursive;
    font-size: 44px;
    line-height: 52px;
  }
  .flavour-rule {
    width: 50px;
    height: 2px;
    border-top: 1px solid var(--ink);
    border-bottom: 1px solid var(--ink);
  }
  .product-name {
    font-family: "Bebas Neue", sans-serif;
    font-size: 98px;
    line-height: 84px;
    transform: scaleX(0.74);
    margin: 0;
  }
  .name-rule {
    width: 100px;
    height: 0;
    border-top: 1px solid var(--ink);
    margin: 6px auto 4px;
  }
  .tagline {
    font-family: "Lobster", cursive;
    font-size: 24px;
    line-height: 30px;
  }
  .wheat {
    position: absolute;
    top: 171px;
    width: 100px;
    height: 150px;
    background: linear-gradient(180deg, #3a3a3a, var(--wheat-fill));
    border-radius: 50px 50px 6px 6px;
  }
  .wheat-left { left: 13px; }
  .wheat-right { left: 484px; }
  .badge {
    position: absolute;
    left: 458px;
    top: 81px;
    width: 72px;
    height: 72px;
  }
</style>
</head>
<body>
  <main class="bag">
    <div class="top-band"><div class="double-rule"></div></div>
    <div class="window"></div>
    <section class="panel">
      <div class="double-rule rule-left"></div>
      <div class="double-rule rule-right"></div>
      <h1 class="brand-name">Dorne's Bakery</h1>

      <svg class="badge" viewBox="0 0 72 72" role="img" aria-label="Certification badge">
        <circle cx="36" cy="36" r="34" fill="none" stroke="var(--ink)" stroke-width="3"/>
        <circle cx="36" cy="36" r="26" fill="none" stroke="var(--ink)" stroke-width="1.5"/>
      </svg>

      <div class="wheat wheat-left" role="img" aria-label="Wheat stalks illustration"></div>
      <div class="wheat wheat-right" role="img" aria-label="Wheat stalks illustration"></div>

      <div class="product">
        <div class="product-flavour">
          <span class="flavour-rule"></span>
          <span>Coconut</span>
          <span class="flavour-rule"></span>
        </div>
        <h2 class="product-name">CREAM BREAD</h2>
        <div class="name-rule"></div>
        <div class="tagline">Freshly Backed</div>
      </div>

      <div class="double-rule rule-bottom"></div>
    </section>
  </main>
</body>
</html>
```